Erstellung eines Polizeiwimpels für Kinder
Zielgruppe
Wir stellen Fahrradwimpel für Kinder her. Hier finden Sie unsere Produkte: https://www.kramladen.de/stores/node/58203916472
Aufgabenstellung
Wir möchten einen 'Polizeiwimpel' für Kinder herstellen.
Wenn möglich, nur eine Farbe verwenden (reduziert Kosten in der Produktion). Der Hintergrund soll 'Polizei Blau' sein.
Wimpelgröße: 17,5 cm X 32 cm X 32cm (Dreieckig)
Ich habe ein selbst erstelltes Design hochgeladen. Es soll den Schriftzug 'Polizei' enthalten und evtl. noch 'Polizei Symbole', die Jungs (und ihre Eltern) ansprechen. (Pistole, Sheriffstern, etc.) Das offizielle Wappen oder andere Hoheitssymbole dürfen wir allerdings nicht verwenden.

```html
<!DOCTYPE html>
<html lang="de">
<head>
<meta charset="utf-8">
<title>Polizeiwimpel</title>
<link href="https://fonts.googleapis.com/css2?family=Arimo:wght@400;700&display=swap" rel="stylesheet">
<style>
  :root {
    --police-blue: #253570;
    --marking-white: #ffffff;
    --page-bg: #ffffff;
  }
  html, body {
    margin: 0;
    padding: 0;
    width: 1200px;
    height: 728px;
    overflow: hidden;
    background: var(--page-bg);
  }
  .pennant {
    display: block;
    width: 1200px;
    height: 728px;
  }
  .pennant-body {
    fill: var(--police-blue);
  }
  .lane-marking {
    stroke: var(--marking-white);
    stroke-width: 10;
    stroke-dasharray: 90 24;
    fill: none;
  }
  .pennant-title {
    font-family: "Arimo", Arial, sans-serif;
    font-weight: 700;
    font-size: 150px;
    fill: var(--marking-white);
  }
  .pennant-url {
    font-family: "Arimo", Arial, sans-serif;
    font-weight: 400;
    font-size: 21px;
    fill: var(--marking-white);
  }
</style>
</head>
<body>
  <svg class="pennant" viewBox="0 0 1200 728" xmlns="http://www.w3.org/2000/svg">
    <polygon class="pennant-body" points="36,56 1136,356 36,656"/>
    <line class="lane-marking lane-marking--top" x1="68" y1="100" x2="920" y2="320"/>
    <line class="lane-marking lane-marking--bottom" x1="68" y1="648" x2="920" y2="378"/>
    <text class="pennant-title" x="118" y="404">Polizei</text>
    <text class="pennant-url" x="70" y="590" transform="rotate(-17 70 590)">www.radfahnen.bike</text>
  </svg>
</body>
</html>
```